one pager for investors

I will give an initial file in any format needed. Also, the photo that must be included. As well as the logo, that must be the key to the overall design in terms of font, colors, and general layout. I will attach a file in PDF format, which is a one pager presenting a project for investors that I would like to attract and convinced to invest in my project. What I would like you to do is propose me different and better design options, taking my first draft as an example. But you must absolutely keep every single word and number, absolutely all the information written in my first draft(except “ TEMPLATE DRAFT”). Also, on the top left corner is the logo of our company, which I think should be your main inspiration document is a one pager presented to potential investors that not only has to include the most important information in order for them to be able to see everything needed to see the value of the project (which I’ve already taken care of by writing the text needed, numbers presented and timeline shown; all of which which must be preserved in terms of content, but can be completely redesigned and manipulated ) sh a.k.a. Project summary for investor to go for it.
Serious rich investors
Real eatate

```html
<!DOCTYPE html>
<html lang="fr">
<head>
<meta charset="utf-8">
<title>Projet immobilier XXX – Synthèse investisseur</title>
<link href="https://fonts.googleapis.com/css2?family=Montserrat:wght@400;500;600;700;800;900&display=swap" rel="stylesheet">
<style>
  :root{
    --navy:#0b1630;
    --blue:#3a56a5;
    --blue-text:#2c4593;
    --row-light:#e4e9f8;
    --row-grey:#e2e2e2;
    --ink:#1a1a1a;
    --title-grey:#3b3b3b;
    --white:#ffffff;
    --page-bg:#ffffff;
  }
  *{margin:0;padding:0;box-sizing:border-box;}
  html,body{width:883px;height:1200px;overflow:hidden;background:var(--page-bg);}
  body{font-family:"Montserrat",sans-serif;color:var(--ink);}
  .page{position:relative;width:883px;height:1200px;overflow:hidden;background:var(--white);}
  .abs{position:absolute;}

  /* header */
  .brand-panel{left:508px;top:0;width:375px;height:205px;background:var(--navy);}
  .brand{left:545px;top:56px;display:flex;align-items:center;gap:18px;color:var(--white);}
  .brand-square{width:42px;height:42px;border:3px solid var(--blue);}
  .brand-name{font-weight:600;font-size:26px;letter-spacing:3px;line-height:1;}
  .brand-name small{display:block;font-size:9px;letter-spacing:4px;margin-top:8px;font-weight:600;}

  .title{left:56px;top:60px;font-weight:900;font-size:44px;color:var(--navy);letter-spacing:-0.5px;line-height:1;}
  .subtitle{left:56px;top:110px;font-weight:800;font-size:30px;color:var(--title-grey);line-height:1;}
  .project-code{left:56px;top:148px;font-weight:900;font-size:46px;color:var(--blue);line-height:1;}
  .title-rule{left:222px;top:188px;width:336px;height:1.5px;background:var(--blue);}

  .hero{left:70px;top:204px;width:813px;height:301px;
    background:linear-gradient(160deg,#c9cfd6 0%,#a99a86 35%,#8d6a55 55%,#5c6b44 80%,#4a5a36 100%);}
  .frame-v{left:56px;top:265px;width:1.5px;height:255px;background:var(--blue);}
  .frame-h{left:56px;top:518px;width:827px;height:1.5px;background:var(--blue);}

  /* description */
  .section-head{font-weight:800;font-size:17px;color:var(--blue-text);line-height:1;}
  .desc-head{left:55px;top:542px;}
  .desc-body{left:55px;top:565px;width:432px;font-size:11.2px;line-height:13.6px;color:#111;}
  .duration{left:57px;top:670px;font-weight:700;font-size:12.5px;color:var(--blue-text);}

  /* financial plan */
  .plan-head{left:57px;top:690px;}
  .fin-group{left:56px;width:381px;}
  .fin-row{display:flex;height:27px;align-items:stretch;}
  .fin-label{width:246px;border-left:1px solid #6f83c2;border-right:1px solid #6f83c2;border-bottom:1px solid #b9c4e6;
    display:flex;align-items:center;padding-left:14px;font-size:11px;font-weight:600;color:var(--blue-text);background:var(--white);}
  .fin-row:first-child .fin-label{border-top:1px solid #6f83c2;}
  .fin-row:last-child .fin-label{border-bottom:1px solid #6f83c2;}
  .fin-label.is-total{background:var(--row-light);color:var(--navy);font-weight:700;}
  .fin-label.is-grey{background:var(--row-grey);color:var(--navy);font-weight:700;}
  .fin-value{width:135px;margin:3px 0;border-radius:0 12px 12px 0;display:flex;align-items:center;padding-left:20px;
    font-size:11px;color:var(--white);}
  .fin-value.dark{background:var(--navy);}
  .fin-value.light{background:var(--blue);}
  .fin-value.bold{font-weight:700;}

  /* investment structure */
  .invest-head{left:510px;top:520px;width:373px;height:47px;background:var(--navy);color:var(--white);
    font-weight:800;font-size:14px;display:flex;align-items:center;padding-left:28px;}
  .invest-panel{left:510px;top:567px;width:373px;height:417px;background:var(--blue);color:var(--white);}
  .metric{position:absolute;text-align:center;text-transform:uppercase;}
  .metric-label{font-weight:700;font-size:10.5px;line-height:11px;color:#e4e8f5;}
  .metric-value{font-weight:700;font-size:22px;line-height:23px;margin-top:8px;}
  .metric-big-label{font-weight:800;font-size:15.5px;line-height:16px;color:#e4e8f5;}
  .metric-note{font-size:10px;line-height:11px;color:#e4e8f5;font-weight:500;}
  .dash-h{position:absolute;height:0;border-top:1px dashed #d6dcf0;}
  .dash-v{position:absolute;width:0;border-left:1px dashed #d6dcf0;}

  /* footer */
  .footer-band{left:175px;top:1097px;width:708px;height:103px;background:var(--navy);}
  .footer-square{left:60px;top:1097px;width:108px;height:103px;border:6px solid var(--blue);background:var(--white);}
  .footer-title{left:198px;top:1131px;font-weight:800;font-size:30px;color:var(--blue);line-height:1;}
  .footer-address{left:480px;top:1119px;color:var(--white);font-size:11.5px;line-height:15px;display:flex;gap:6px;}
  .footer-divider{left:689px;top:1117px;width:1px;height:50px;background:#c9cfe2;}
  .footer-contacts{left:727px;top:1120px;color:var(--white);font-size:11.5px;line-height:16px;}
  .contact-line{display:flex;align-items:center;gap:6px;margin-left:-18px;}
  .dot-icon{width:12px;height:12px;flex:none;}
</style>
</head>
<body>
<main class="page">

  <div class="abs brand-panel"></div>
  <div class="abs brand">
    <div class="brand-square"></div>
    <div class="brand-name">VALMORE<small>PROPERTIES SA</small></div>
  </div>

  <h1 class="abs title">CONFIDENTIEL</h1>
  <h2 class="abs subtitle">PROJET IMOBILIER</h2>
  <div class="abs project-code">“XXX”</div>
  <div class="abs title-rule"></div>

  <div class="abs hero" role="img" aria-label="Rendu architectural d’un immeuble résidentiel en terrasses avec balcons vitrés et jardin arboré"></div>
  <div class="abs frame-v"></div>
  <div class="abs frame-h"></div>

  <h3 class="abs section-head desc-head">DESCRIPTION DU PROJET</h3>
  <p class="abs desc-body">Le projet XXX est un projet de dévloppement de 30 appartements de standing en PPE au centre de Lausanne. Le terrain a été sécurisé par la signature du vente à terme conditionnelle. L’objectif est d’obtenir le permis de construire, puis de ventre les lots. Dans un premier temps sur plan puis aufil de laconstruction.</p>
  <p class="abs duration">Durée estimée du projet–24 à 36 mois</p>

  <h3 class="abs section-head plan-head">PLAN FINANCIER</h3>

  <div class="abs fin-group" style="top:707px">
    <div class="fin-row"><div class="fin-label">PRIX DU TERRAIN</div><div class="fin-value dark">CHF 2,000,000</div></div>
    <div class="fin-row"><div class="fin-label">FRAIS D'ACQUISITION</div><div class="fin-value light">CHF 100,000</div></div>
    <div class="fin-row"><div class="fin-label">COÛT DE CONSTRUCTION</div><div class="fin-value dark">CHF 2,500,000</div></div>
    <div class="fin-row"><div class="fin-label">DIVERS &amp; IMPRÉVUS</div><div class="fin-value light">CHF 200,000</div></div>
    <div class="fin-row"><div class="fin-label is-total">PRIX DE REVIENT TOTAL</div><div class="fin-value dark bold">CHF 4,800,000</div></div>
  </div>

  <div class="abs fin-group" style="top:851px">
    <div class="fin-row"><div class="fin-label is-total">PRIX DE VENTE TOTAL</div><div class="fin-value dark bold">CHF 7,500,000</div></div>
    <div class="fin-row"><div class="fin-label">FRAIS DE VENTE</div><div class="fin-value light">CHF 190,000</div></div>
  </div>

  <div class="abs fin-group" style="top:922px">
    <div class="fin-row"><div class="fin-label is-total">MARGE DU PROJET</div><div class="fin-value dark bold">CHF 2,510,000</div></div>
    <div class="fin-row"><div class="fin-label is-grey">EN % DU PRIX DE VENTE</div><div class="fin-value light bold">33.47%</div></div>
  </div>

  <div class="abs invest-head">STRUCTURE D’INVESTISSEMENT</div>
  <section class="abs invest-panel">
    <div class="metric" style="left:18px;width150px;width:150px;top:22px">
      <div class="metric-label">BESOIN DE FONDS<br>PROPRES</div>
      <div class="metric-value">CHF<br>2’000’000</div>
    </div>
    <div class="metric" style="left:186px;width:150px;top:22px">
      <div class="metric-label">RETOUR DE<br>FONDS TOTAL</div>
      <div class="metric-value">CHF<br>3’156’600</div>
    </div>
    <div class="dash-v" style="left:181px;top:22px;height:102px"></div>
    <div class="dash-h" style="left:29px;top:131px;width:140px"></div>
    <div class="dash-h" style="left:193px;top:131px;width:122px"></div>

    <div class="metric" style="left:0;width:373px;top:158px">
      <div class="metric-big-label">BÉNÉFICE NET INVESTISSEUR</div>
      <div class="metric-value" style="margin-top:5px">CHF 1’656’600</div>
      <div class="metric-note" style="margin-top:4px">SOIT 2/3 DU&nbsp; BÉNÉFICE PROJET</div>
    </div>
    <div class="dash-h" style="left:29px;top:253px;width:140px"></div>
    <div class="dash-h" style="left:193px;top:253px;width:122px"></div>
    <div class="dash-v" style="left:181px;top:259px;height:132px"></div>

    <div class="metric" style="left:14px;width:158px;top:287px">
      <div class="metric-big-label">MULTIPLE<br>SUR FONDS<br>PROPRES</div>
      <div class="metric-value" style="margin-top:6px">CHF<br>X1.83</div>
    </div>
    <div class="metric" style="left:186px;width:150px;top:287px">
      <div class="metric-big-label">RENDEMENT<br>ANNUALISÉ</div>
      <div class="metric-value" style="margin-top:8px">41.4%</div>
      <div class="metric-note" style="margin-top:10px">CALCUL SUR<br>24 MOIS</div>
    </div>
  </section>

  <svg class="abs" style="left:0;top:1005px" width="883" height="75" viewBox="0 0 883 75" role="list" aria-label="Calendrier du projet">
    <g font-family="Montserrat, sans-serif" font-weight="700" font-size="11.5" text-anchor="middle">
      <path d="M73 11 H177 L194 25 L177 39 H73 A14 14 0 0 1 73 11 Z" fill="var(--blue)"/>
      <path d="M210 11 H337 L355 25 L337 39 H210 A14 14 0 0 1 210 11 Z" fill="var(--navy)"/>
      <path d="M371 11 H530 L549 25 L530 39 H371 A14 14 0 0 1 371 11 Z" fill="var(--blue)"/>
      <path d="M564 11 H769 L789 25 L769 39 H564 A14 14 0 0 1 564 11 Z" fill="var(--navy)"/>
      <line x1="789" y1="25" x2="962" y2="25" stroke="var(--blue)" stroke-width="2"/>
      <line x1="785" y1="25" x2="962" y2="25" stroke="var(--blue)" stroke-width="2"/>
      <path d="M955 17 L971 25 L955 33 Z" fill="var(--blue)" transform="translate(-3 0)"/>
      <text x="128" y="29" fill="#fff">08.2024</text>
      <text x="272" y="29" fill="#fff">04.2025</text>
      <text x="452" y="29" fill="#fff">12.2025</text>
      <text x="669" y="29" fill="#fff">12.2025</text>
      <g stroke="var(--navy)" stroke-width="2">
        <line x1="128" y1="39" x2="128" y2="47"/><line x1="272" y1="39" x2="272" y2="47"/>
        <line x1="452" y1="39" x2="452" y2="47"/><line x1="669" y1="39" x2="669" y2="47"/>
      </g>
      <g fill="var(--navy)" font-size="11">
        <text x="128" y="66">ACHAT PARCELLE</text>
        <text x="276" y="66">MISE À L’ENQUÊTE</text>
        <text x="452" y="66">DÉBUT CONSTRUCTION</text>
        <text x="669" y="66">LIVRAISON</text>
      </g>
    </g>
  </svg>

  <footer>
    <div class="abs footer-band"></div>
    <div class="abs footer-square"></div>
    <div class="abs footer-title">CONFIDENTIEL</div>
    <div class="abs footer-address">
      <svg class="dot-icon" viewBox="0 0 12 12" style="margin-top:2px"><circle cx="6" cy="6" r="6" fill="var(--blue)"/><path d="M6 2.5a2 2 0 0 1 2 2c0 1.5-2 4-2 4s-2-2.5-2-4a2 2 0 0 1 2-2z" fill="#fff"/></svg>
      <div>Valmore Properties Vaud SA<br>Avenue des Tilleuls<br>4 -CH 1170 Aubonne</div>
    </div>
    <div class="abs footer-divider"></div>
    <div class="abs footer-contacts">
      <div class="contact-line"><svg class="dot-icon" viewBox="0 0 12 12"><circle cx="6" cy="6" r="6" fill="var(--blue)"/><path d="M4 3l1.2 1.6-.6.8a5 5 0 0 0 2 2l.8-.6L9 8l-.8 1C6 9 3 6 3 3.8z" fill="#fff"/></svg>079 000 12 34</div>
      <div class="contact-line"><svg class="dot-icon" viewBox="0 0 12 12"><circle cx="6" cy="6" r="6" fill="var(--blue)"/><circle cx="6" cy="6" r="3" fill="none" stroke="#fff" stroke-width="1"/><line x1="3" y1="6" x2="9" y2="6" stroke="#fff" stroke-width="1"/></svg>www.valmore-example.ch</div>
      <div class="contact-line"><svg class="dot-icon" viewBox="0 0 12 12"><circle cx="6" cy="6" r="6" fill="var(--blue)"/><rect x="3" y="4" width="6" height="4" fill="none" stroke="#fff" stroke-width="1"/><path d="M3 4l3 2.2L9 4" fill="none" stroke="#fff" stroke-width="1"/></svg>info@valmore-example.ch</div>
    </div>
  </footer>

</main>
</body>
</html>
```